Business card design for crowd sourced review site.

I need a business card magnet design for an online, crowd-sourced, restaurant review site strictly for Kosher restaurants.
It is similar to RoamLedger but catering to a very particular crowd.
The markets it will be distributed in are flooded with business card fridge magnets so this needs to be eye-catching and unique. The Business name is PlateMarks
The website isnt finished but you can see the basic setup here
http://restaurant.vintrello.com/

The second image i included is another logo design I liked and was thinking about using and decided I will probably also make a SECOND custom cut business card in the shape of that icon. Bonus if you can throw that in also.

Target Market(s)

Jewish consumers aged 20-35

Industry/Entity Type

Business

Contact Information for Business Card

see description.
Design should not be too crowded and should in eye-catching. Will mainly be used as fridge magnets.

Requirements
Must have
• Website address. logo.
Nice to have
• tagline. (The Definitive guide to kosher dining for the Kosher consumer)
• Im not a professional but I personally think the color blue goes along with this concept. ill leave it to you to decide.
Should not have
• any religious symbols.

```html
<!DOCTYPE html>
<html lang="en">
<head>
<meta charset="utf-8">
<title>PlateMarks Business Card</title>
<link rel="stylesheet" href="https://fonts.googleapis.com/css2?family=Courgette&family=Open+Sans:wght@400;600;700&display=swap">
<style>
  :root {
    --page-bg: #ece9e4;
    --card-black: #0d0d0d;
    --card-black-soft: #1c1c1c;
    --brand-red: #e03a24;
    --brand-red-deep: #c92b18;
    --white: #ffffff;
    --grill-dark: #2a1410;
    --grill-mid: #7a2a18;
    --grill-warm: #b8452a;
  }
  * { margin: 0; padding: 0; box-sizing: border-box; }
  html, body {
    width: 1200px; height: 900px; overflow: hidden;
    background: var(--page-bg);
    font-family: "Open Sans", Arial, sans-serif;
  }
  .sheet {
    position: relative; width: 1200px; height: 900px;
    display: flex; align-items: center; justify-content: center; gap: 40px;
  }
  .card {
    position: relative; width: 540px; height: 310px; overflow: hidden;
    box-shadow: 0 6px 18px rgba(0,0,0,0.18);
  }
  .card-front {
    background: radial-gradient(ellipse at 55% 45%, var(--grill-warm) 0%, var(--grill-mid) 45%, var(--grill-dark) 100%);
  }
  .card-back {
    background: radial-gradient(ellipse at 40% 30%, var(--card-black-soft) 0%, var(--card-black) 70%);
  }
  .card-back .wave { position: absolute; inset: 0; width: 100%; height: 100%; }
  .brand {
    position: absolute; top: 44px; right: 36px;
    display: flex; align-items: center; gap: 8px;
    color: var(--white); font-weight: 600; font-size: 22px; letter-spacing: 0.2px;
  }
  .brand-dot { width: 14px; height: 14px; border-radius: 50%; background: var(--brand-red); }
  .person { position: absolute; top: 66px; left: 32px; }
  .person-name {
    font-family: "Courgette", cursive; color: var(--brand-red);
    font-size: 29px; line-height: 1.1;
  }
  .person-title { color: var(--white); font-size: 14px; margin-top: 2px; }
  .contact { position: absolute; top: 132px; left: 32px; list-style: none; }
  .contact li {
    display: flex; align-items: center; gap: 8px;
    color: var(--white); font-size: 15px; line-height: 22px;
  }
  .contact svg { width: 11px; height: 11px; fill: var(--brand-red); }
  .tagline {
    position: absolute; top: 186px; left: 32px;
    color: var(--brand-red); font-weight: 700; font-size: 13.5px;
  }
  .website {
    position: absolute; bottom: 22px; right: 28px;
    color: var(--white); font-size: 13px;
  }
</style>
</head>
<body>
<main class="sheet">
  <section class="card card-front" role="img" aria-label="Photograph of steaks, grilled tomatoes and vegetable skewers on a barbecue grill"></section>

  <section class="card card-back">
    <svg class="wave" viewBox="0 0 540 310" preserveAspectRatio="none" aria-hidden="true">
      <path d="M0 276 C 190 300, 370 262, 540 200 L540 310 L0 310 Z" fill="var(--white)"/>
      <path d="M0 296 C 210 318, 385 272, 540 212 L540 310 L0 310 Z" fill="var(--brand-red)"/>
    </svg>

    <div class="brand"><span class="brand-dot"></span>PlateMarks</div>

    <div class="person">
      <h1 class="person-name">Daniel Harper</h1>
      <p class="person-title">Managing Director</p>
    </div>

    <ul class="contact">
      <li><svg viewBox="0 0 12 12"><path d="M2 1 L4.5 1 L5.5 3.5 L4 4.5 C4.6 6 6 7.4 7.5 8 L8.5 6.5 L11 7.5 L11 10 C11 10.6 10.6 11 10 11 C5 11 1 7 1 2 C1 1.4 1.4 1 2 1 Z"/></svg>(044)987654321</li>
      <li><svg viewBox="0 0 12 12"><path d="M1 2.5 H11 V9.5 H1 Z M1.5 3 L6 6.5 L10.5 3" stroke="var(--card-black)" stroke-width="0.8"/></svg>info@platemarks-mail.com</li>
    </ul>

    <p class="tagline">The Definitive guide to kosher dining for the Kosher consumer</p>

    <p class="website">www.restaurant.vintrello.com</p>
  </section>
</main>
</body>
</html>
```